A new presentation to our clients

we are a Real Estate agency, our website is www.dorelumia.com and it’s time to have a new, fashion and remarcable Business Card. we want to differentiate ourselves from other companies so we want a business card that differentiates us. we want the business card to impact our customers. in the competitive market that we have today, we have to be different and it is this difference that we seek

Target Market(s)

Real Estate Clients

Contact Information for Business Card

We search a totaly diferent card from the usual

Font styles to use
Sans Serif

Colors
e34197

Requirements
Must have
• Logo, adress, phone contact, e-mail, photo, and our website
Nice to have
• We would like to see a modern business card
Should not have
• Houses or building draws

```html
<!DOCTYPE html>
<html lang="en">
<head>
<meta charset="utf-8">
<title>Dore Lumia — Business Card</title>
<link href="https://fonts.googleapis.com/css2?family=Lato:wght@400;700&display=swap" rel="stylesheet">
<style>
  :root {
    --page-bg: #e9e9e9;
    --card-bg: #fbfbfa;
    --brand: #e0156a;
    --edge: #c40e4f;
    --ink: #2b2b2b;
    --pattern-tone: #ececec;
  }
  html, body {
    margin: 0;
    padding: 0;
    width: 1200px;
    height: 1021px;
    overflow: hidden;
    background: var(--page-bg);
    font-family: "Lato", sans-serif;
  }
  .canvas {
    position: relative;
    width: 1200px;
    height: 1021px;
  }
  .card {
    position: absolute;
    left: 250px;
    width: 700px;
    height: 400px;
    background: var(--card-bg);
    border-bottom: 6px solid var(--edge);
    box-shadow: 0 10px 24px rgba(0,0,0,0.12);
    box-sizing: border-box;
  }
  .card--front { top: 70px; }
  .card--back { top: 545px; }

  .front-texture {
    position: absolute;
    inset: 0;
    background: linear-gradient(135deg, #f6f6f5 0%, var(--pattern-tone) 100%);
  }
  .brand-name {
    margin: 0;
    color: var(--brand);
    font-weight: 700;
    letter-spacing: 1px;
    white-space: nowrap;
  }
  .card--front .brand-name {
    position: absolute;
    left: 0; right: 0;
    top: 50%;
    transform: translateY(-50%);
    text-align: center;
    font-size: 64px;
  }

  .back-layout {
    position: absolute;
    inset: 0;
    display: flex;
    flex-direction: column;
    align-items: center;
    justify-content: center;
  }
  .card--back .brand-name { font-size: 34px; }
  .divider {
    width: 70px;
    height: 2px;
    background: var(--brand);
    margin: 22px 0;
  }
  .contact-address,
  .contact-row {
    display: flex;
    align-items: center;
    gap: 22px;
    font-size: 15px;
    color: var(--ink);
  }
  .contact-address { margin-bottom: 10px; }
  .contact-item {
    display: flex;
    align-items: center;
    gap: 6px;
  }
  .contact-item svg {
    width: 13px;
    height: 13px;
    fill: var(--brand);
  }
</style>
</head>
<body>
<main class="canvas">
  <section class="card card--front" aria-label="Card front">
    <div class="front-texture" role="img" aria-label="Faint repeating monogram pattern in light grey"></div>
    <h1 class="brand-name">Dore Lumia</h1>
  </section>

  <section class="card card--back" aria-label="Card back">
    <div class="back-layout">
      <h2 class="brand-name">Dore Lumia</h2>
      <div class="divider"></div>
      <div class="contact-address">
        <span class="contact-item">
          <svg viewBox="0 0 16 16" aria-hidden="true"><path d="M8 0a5.5 5.5 0 0 0-5.5 5.5C2.5 10 8 16 8 16s5.5-6 5.5-10.5A5.5 5.5 0 0 0 8 0zm0 7.8a2.3 2.3 0 1 1 0-4.6 2.3 2.3 0 0 1 0 4.6z"/></svg>
          your address here
        </span>
      </div>
      <div class="contact-row">
        <span class="contact-item">
          <svg viewBox="0 0 16 16" aria-hidden="true"><path d="M3.6 1l2.3 3-1.4 1.6c.8 1.9 2.1 3.2 4 4l1.6-1.4 3 2.3-1.6 2.7C6.3 12.9 3 9.6 1 4.3z"/></svg>
          000 000 0000
        </span>
        <span class="contact-item">
          <svg viewBox="0 0 16 16" aria-hidden="true"><path d="M1 3h14v10H1zm1.2 1.2L8 8.6l5.8-4.4z"/></svg>
          yourmail@xyz.com
        </span>
        <span class="contact-item">
          <svg viewBox="0 0 16 16" aria-hidden="true"><path d="M8 1a7 7 0 1 0 0 14A7 7 0 0 0 8 1zm0 1.4c.7.8 1.3 2 1.6 3.4H6.4C6.7 4.4 7.3 3.2 8 2.4zM2.6 9.5a5.6 5.6 0 0 1 0-3h2.3a11 11 0 0 0 0 3zm3.8 0a9 9 0 0 1 0-3h3.2a9 9 0 0 1 0 3zm4.7 0a11 11 0 0 0 0-3h2.3a5.6 5.6 0 0 1 0 3zM8 13.6c-.7-.8-1.3-2-1.6-3.4h3.2c-.3 1.4-.9 2.6-1.6 3.4z"/></svg>
          www.dorelumia.com
        </span>
      </div>
      <div class="divider"></div>
    </div>
  </section>
</main>
</body>
</html>
```